Web Design

We are Carvonta’s new and used car supermarket, we need a clean and nice look web design.

What included on homepage:
1. Logo
2. Slideshow (additional)
3. Menu - Home, About us, New cars, Used cars, Contact us
4. Advance Search
5. Customer Reviews
6. Social links - facebook, twitter , youtube
7. Banner Ads
8. Recent News
9. Newsletter

We just need psd files, home and contact us.

Industry/Entity Type

Used Car

Number of Pages Required

2 page

Requirements
Must have
• Webpage are well designed and in accordance with the color of the logo that is displayed in the file attachment.

```html
<!DOCTYPE html>
<html lang="en">
<head>
<meta charset="utf-8">
<title>Carvonta Car Supermarket</title>
<link href="https://fonts.googleapis.com/css2?family=Roboto+Condensed:wght@400;700&family=Roboto:wght@400;500;700&display=swap" rel="stylesheet">
<style>
:root{
  --blue:#0a60b6;
  --blue-dark:#0b4f98;
  --red:#ee1b2e;
  --yellow:#f7b21d;
  --green:#3f9a16;
  --ink:#333;
  --muted:#777;
  --line:#dcdcdc;
  --page:#f0f0f0;
  --panel:#fff;
  --footer:#4b4b4b;
}
*{box-sizing:border-box;margin:0;padding:0}
html,body{width:1163px;height:1200px;overflow:hidden;background:var(--page);font-family:"Roboto",sans-serif;color:var(--ink)}
.canvas{position:relative;width:1163px;height:1200px}
.abs{position:absolute}
.cond{font-family:"Roboto Condensed",sans-serif}
.page{left:218px;top:16px;width:727px;height:1026px;background:var(--panel);border:1px solid #e6e6e6}
.logo{left:234px;top:44px;color:var(--blue);font-family:"Roboto",sans-serif;font-weight:500;font-size:28px;line-height:1}
.logo-tag{left:235px;top:74px;color:#666;font-family:"Roboto",sans-serif;font-size:10px;letter-spacing:1px}
.tollfree{left:492px;top:64px;font-family:"Roboto Condensed",sans-serif;font-size:21px;color:#444}
.search-box{left:688px;top:60px;width:132px;height:31px;border:1px solid var(--line);font-size:9px;color:#888;padding:10px 0 0 26px}
.search-btn{left:820px;top:60px;width:29px;height:31px;background:var(--red);display:flex;align-items:center;justify-content:center}
.social{width:20px;height:20px;border-radius:50%;background:#111}
.ticker{left:218px;top:107px;width:727px;height:31px;background:var(--blue);color:#fff;font-size:8.6px}
.ticker-label{left:0;top:0;width:94px;height:31px;background:var(--yellow);color:#333;font-family:"Roboto Condensed",sans-serif;font-size:12px;display:flex;align-items:center;justify-content:center}
.ticker-text{left:130px;top:10px;width:490px;white-space:nowrap;overflow:hidden;letter-spacing:-.15px}
.login{left:633px;top:0;width:37px;height:31px;background:var(--yellow);color:#333;font-family:"Roboto Condensed",sans-serif;font-size:12px;display:flex;align-items:center;justify-content:center}
.register{left:670px;top:0;width:57px;height:31px;background:var(--red);font-family:"Roboto Condensed",sans-serif;font-size:12px;display:flex;align-items:center;justify-content:center}
.nav{left:218px;top:138px;width:727px;height:34px;border-bottom:1px solid #e4e4e4;background:#f8f8f8;display:flex;justify-content:center;font-family:"Roboto Condensed",sans-serif;font-size:11.5px}
.nav a{color:#333;text-decoration:none;padding:0 12px;display:flex;align-items:center;border-right:1px solid #e4e4e4}
.nav a:last-child{border-right:0}
.nav a.active{background:var(--blue);color:#fff}
.photo{background:linear-gradient(135deg,#e9e9e9,#bfc3c7)}
.frame{border:1px solid var(--line);padding:4px;background:#fff}
.frame .photo{width:100%;height:100%}
.tab{font-family:"Roboto Condensed",sans-serif;font-size:11.5px;display:flex;align-items:center;justify-content:center}
.tab.plain{border:1px solid var(--line);border-bottom:0;background:#fff;color:#333}
.tab.blue{background:var(--blue);color:#fff}
.tab.green{background:var(--green);color:#fff}
.search-panel{left:600px;top:207px;width:333px;height:234px;border:1px solid var(--line)}
.lbl{font-family:"Roboto Condensed",sans-serif;font-size:10.5px;color:#444}
.sel{height:20px;border:1px solid var(--line);font-size:8.5px;color:#aaa;padding:5px 0 0 7px}
.sel::after{content:"";position:absolute;right:0;top:0;width:19px;height:18px;border-left:1px solid var(--line)}
.sel i{position:absolute;right:6px;top:8px;border:3.5px solid transparent;border-top:4px solid #666}
.btn{font-family:"Roboto Condensed",sans-serif;font-size:11.5px;color:#fff;display:flex;align-items:center;justify-content:center}
.listing{left:232px;top:485px;width:519px;height:219px;border:1px solid var(--line)}
.car{position:absolute;width:170px;height:62px}
.car .photo{position:absolute;left:0;top:0;width:60px;height:49px}
.car .info{position:absolute;left:75px;top:-2px;font-size:8.8px;color:#888;line-height:14px}
.car .info b{display:block;font-family:"Roboto Condensed",sans-serif;font-weight:400;font-size:10.5px;color:#333}
.rowline{position:absolute;height:1px;background:var(--line)}
.hot{left:762px;top:485px;width:171px;height:218px;background:#e7e7e7}
.hot-title{left:776px;top:627px;color:var(--blue-dark);font-family:"Roboto Condensed",sans-serif;font-weight:700;font-size:10px}
.hot-text{left:776px;top:640px;width:150px;font-size:8px;color:#777;line-height:11.5px}
.hot-meta{font-size:8.8px;color:#444}
.box{border:1px solid var(--line)}
.box-head{position:absolute;left:0;top:0;height:30px;background:#f1f1f1;font-family:"Roboto Condensed",sans-serif;font-size:11.5px;display:flex;align-items:center;padding-right:12px}
.box-head .ico{width:26px;height:30px;background:#555;margin-right:8px;display:flex;align-items:center;justify-content:center}
.readmore{position:absolute;right:16px;top:10px;color:var(--green);font-size:8px;font-weight:700}
.para{position:absolute;left:14px;width:230px;font-size:8.8px;color:#777;line-height:15px;letter-spacing:-.1px}
.dash{position:absolute;left:14px;width:228px;border-top:1px dotted #c8c8c8}
.help{left:762px;top:718px;width:171px;height:112px;background:var(--blue);color:#fff;text-align:center}
.help-head{height:28px;background:var(--blue-dark);font-family:"Roboto Condensed",sans-serif;font-weight:700;font-size:10px;display:flex;align-items:center;padding-left:44px;position:relative}
.tuned{left:762px;top:838px;width:171px;height:63px;background:var(--yellow);text-align:center;font-family:"Roboto Condensed",sans-serif;font-size:11px;color:#333}
.newsletter-band{left:0;top:1042px;width:1163px;height:72px;background:#eef0f4}
.nl-title{left:233px;top:1059px;width:260px;white-space:nowrap;font-family:"Roboto Condensed",sans-serif;font-size:15.5px;letter-spacing:-.2px;color:#333}
.nl-sub{left:233px;top:1080px;font-size:8.6px;color:#888}
.nl-form{left:501px;top:1056px;width:428px;height:43px;background:#fff;border:1px solid var(--line)}
.nl-input{left:7px;top:7px;width:305px;height:28px;background:#f2f2f2;border:1px solid #e3e3e3;font-size:8.8px;color:#888;padding:9px 0 0 42px}
.nl-btn{left:312px;top:6px;width:109px;height:29px;background:var(--blue);font-weight:700;font-size:11.5px}
.footer{left:218px;top:1114px;width:727px;height:26px;background:var(--footer);display:flex;justify-content:center;align-items:center;gap:12px;font-size:8px;color:#fff}
.copy{left:218px;top:1140px;width:727px;height:30px;background:#fff;font-size:8px;color:#666;text-align:center;padding-top:10px}
</style>
</head>
<body>
<div class="canvas">
  <div class="abs page"></div>

  <!-- header -->
  <div class="abs logo">Carvonta</div>
  <div class="abs logo-tag">CAR SUPERMARKET</div>
  <div class="abs tollfree">Toll Free : 123456789</div>
  <div class="abs search-box">search your car here</div>
  <div class="abs search-btn"><svg width="11" height="11" viewBox="0 0 11 11"><circle cx="4.3" cy="4.3" r="3.2" fill="none" stroke="#fff" stroke-width="1.6"/><line x1="6.7" y1="6.7" x2="10" y2="10" stroke="#fff" stroke-width="1.8"/></svg></div>
  <div class="abs social" style="left:862px;top:65px"></div>
  <div class="abs social" style="left:888px;top:65px"></div>
  <div class="abs social" style="left:914px;top:65px"></div>

  <div class="abs ticker">
    <div class="abs ticker-label">Latest Updates</div>
    <div class="abs ticker-text">Lorem Ipsum is simply dummy text of the printing and typesetting industry. Lorem Ipsum has been the industry's standard</div>
    <div class="abs login">Login</div>
    <div class="abs register">Register</div>
  </div>

  <nav class="abs nav">
    <a href="#">Home</a><a href="#">About us</a><a href="#">New cars</a><a href="#">Used cars</a><a href="#" class="active">Custoers Reviews</a><a href="#">Recent News</a><a href="#">Contact Us</a>
  </nav>

  <!-- slideshow -->
  <div class="abs frame" style="left:229px;top:180px;width:358px;height:175px"><div class="photo" role="img" aria-label="Silver sedan on white background"></div></div>
  <div class="abs frame" style="left:233px;top:364px;width:81px;height:75px"><div class="photo" role="img" aria-label="Silver car side view"></div></div>
  <div class="abs frame" style="left:323px;top:364px;width:80px;height:75px"><div class="photo" role="img" aria-label="Red sports car detail" style="background:linear-gradient(135deg,#d01a2a,#3a0a10)"></div></div>
  <div class="abs frame" style="left:412px;top:364px;width:81px;height:75px"><div class="photo" role="img" aria-label="Silver car rear view"></div></div>
  <div class="abs frame" style="left:501px;top:364px;width:81px;height:75px"><div class="photo" role="img" aria-label="Grey car front on dark background" style="background:linear-gradient(135deg,#7d8a90,#1e2427)"></div></div>

  <!-- search panel -->
  <div class="abs tab plain" style="left:614px;top:182px;width:89px;height:23px">Search Used Cars</div>
  <div class="abs tab blue" style="left:710px;top:182px;width:88px;height:22px">Search New Cars</div>
  <div class="abs search-panel"></div>

  <div class="abs lbl" style="left:621px;top:224px">Make</div>
  <div class="abs lbl" style="left:781px;top:224px">Model</div>
  <div class="abs sel" style="left:614px;top:240px;width:146px">Any Make<i></i></div>
  <div class="abs sel" style="left:774px;top:240px;width:145px">Any Model<i></i></div>

  <div class="abs lbl" style="left:621px;top:268px">Region</div>
  <div class="abs lbl" style="left:781px;top:268px">Body Type</div>
  <div class="abs sel" style="left:614px;top:285px;width:146px">Any Region<i></i></div>
  <div class="abs sel" style="left:774px;top:285px;width:145px">Any Body Type<i></i></div>

  <div class="abs lbl" style="left:621px;top:311px">Min Year</div>
  <div class="abs lbl" style="left:696px;top:311px">Max Year</div>
  <div class="abs lbl" style="left:781px;top:311px">Min Price</div>
  <div class="abs lbl" style="left:856px;top:311px">Max Price</div>
  <div class="abs sel" style="left:614px;top:328px;width:70px">Min<i></i></div>
  <div class="abs sel" style="left:689px;top:328px;width:71px">Max<i></i></div>
  <div class="abs sel" style="left:774px;top:328px;width:70px">Min<i></i></div>
  <div class="abs sel" style="left:849px;top:328px;width:70px">Max<i></i></div>

  <div class="abs lbl" style="left:621px;top:355px">Transmission</div>
  <div class="abs lbl" style="left:781px;top:355px">Color</div>
  <div class="abs sel" style="left:614px;top:372px;width:146px">Any Transmission<i></i></div>
  <div class="abs sel" style="left:774px;top:372px;width:145px">Any Color<i></i></div>

  <div class="abs btn" style="left:641px;top:406px;width:90px;height:21px;background:var(--blue)">Search</div>
  <div class="abs btn" style="left:801px;top:406px;width:89px;height:21px;background:var(--red)">Advance Search</div>

  <!-- latest cars -->
  <div class="abs tab plain" style="left:246px;top:460px;width:81px;height:25px;color:var(--blue)">Latest New cars</div>
  <div class="abs tab green" style="left:334px;top:460px;width:89px;height:22px">Latest Used cars</div>
  <div class="abs listing">
    <div class="rowline" style="left:14px;top:79px;width:150px"></div>
    <div class="rowline" style="left:188px;top:79px;width:152px"></div>
    <div class="rowline" style="left:353px;top:79px;width:152px"></div>
    <div class="rowline" style="left:14px;top:150px;width:150px"></div>
    <div class="rowline" style="left:188px;top:150px;width:152px"></div>
    <div class="rowline" style="left:353px;top:150px;width:152px"></div>

    <div class="car" style="left:14px;top:16px"><div class="photo" role="img" aria-label="Red hatchback" style="background:linear-gradient(135deg,#c8202c,#5a0d12)"></div><div class="info"><b>Lorem Ipsum</b>Year : 2014<br>Mileage : 39000 ml.<br>Price : $15000</div></div>
    <div class="car" style="left:188px;top:16px"><div class="photo" role="img" aria-label="Red compact car" style="background:linear-gradient(135deg,#f2f2f2,#e02a2a)"></div><div class="info"><b>Lorem Ipsum</b>Year : 2014<br>Mileage : 39000 ml.<br>Price : $15000</div></div>
    <div class="car" style="left:353px;top:16px"><div class="photo" role="img" aria-label="Silver coupe front"></div><div class="info"><b>Lorem Ipsum</b>Year : 2014<br>Mileage : 39000 ml.<br>Price : $15000</div></div>

    <div class="car" style="left:14px;top:86px"><div class="photo" role="img" aria-label="Orange compact car" style="background:linear-gradient(135deg,#f6a23c,#c9611a)"></div><div class="info"><b>Lorem Ipsum</b>Year : 2014<br>Mileage : 39000 ml.<br>Price : $15000</div></div>
    <div class="car" style="left:188px;top:86px"><div class="photo" role="img" aria-label="Silver sedan"></div><div class="info"><b>Lorem Ipsum</b>Year : 2014<br>Mileage : 39000 ml.<br>Price : $15000</div></div>
    <div class="car" style="left:353px;top:86px"><div class="photo" role="img" aria-label="Red car wheel close-up" style="background:linear-gradient(135deg,#e0502e,#3a1a14)"></div><div class="info"><b>Lorem Ipsum</b>Year : 2014<br>Mileage : 39000 ml.<br>Price : $15000</div></div>

    <div class="car" style="left:14px;top:157px"><div class="photo" role="img" aria-label="Dark blue classic car" style="background:linear-gradient(135deg,#2a3a6a,#0c1020)"></div><div class="info"><b>Lorem Ipsum</b>Year : 2014<br>Mileage : 39000 ml.<br>Price : $15000</div></div>
    <div class="car" style="left:188px;top:157px"><div class="photo" role="img" aria-label="Car wheel on a country road" style="background:linear-gradient(135deg,#9bb56a,#3d4a2a)"></div><div class="info"><b>Lorem Ipsum</b>Year : 2014<br>Mileage : 39000 ml.<br>Price : $15000</div></div>
    <div class="car" style="left:353px;top:157px"><div class="photo" role="img" aria-label="Silver sports car"></div><div class="info"><b>Lorem Ipsum</b>Year : 2014<br>Mileage : 39000 ml.<br>Price : $15000</div></div>
  </div>

  <!-- hot offer -->
  <div class="abs tab blue" style="left:803px;top:460px;width:89px;height:22px">Latest Hot Offer</div>
  <div class="abs hot"></div>
  <div class="abs frame" style="left:777px;top:501px;width:137px;height:119px;padding:3px"><div class="photo" role="img" aria-label="Car wheel speeding on a road" style="background:linear-gradient(135deg,#8f9a5a,#2f3520)"></div></div>
  <div class="abs hot-title">Lorem Ipsum</div>
  <div class="abs hot-text">Lorem Ipsum is simply dummy text of the printing and typesetting industry. Lorem</div>
  <div class="abs hot-meta" style="left:776px;top:666px">Year : 2014</div>
  <div class="abs hot-meta" style="left:843px;top:666px;color:var(--green)">Mileage : 39000 ml.</div>
  <div class="abs hot-meta" style="left:776px;top:681px">Price : $15000</div>

  <!-- reviews -->
  <div class="abs box" style="left:232px;top:719px;width:251px;height:183px">
    <div class="box-head"><span class="ico"><svg width="12" height="12" viewBox="0 0 12 12"><path d="M2 10 L2.5 7.5 L8.5 1.5 L10.5 3.5 L4.5 9.5 Z" fill="#fff"/></svg></span>Customer Reviews</div>
    <span class="readmore">Read More</span>
    <p class="para" style="top:45px">Lorem Ipsum is simply dummy text of the printing &amp; type-setting industry. Lorem Ipsum has been the industry's</p>
    <div class="dash" style="top:82px"></div>
    <p class="para" style="top:93px">Lorem Ipsum is simply dummy text of the printing &amp; type-setting industry. Lorem Ipsum has been the industry's</p>
    <div class="dash" style="top:130px"></div>
    <p class="para" style="top:142px">Lorem Ipsum is simply dummy text of the printing &amp; type-setting industry. Lorem Ipsum has been the industry's</p>
  </div>

  <!-- news -->
  <div class="abs box" style="left:493px;top:719px;width:258px;height:183px">
    <div class="box-head"><span class="ico"><svg width="11" height="13" viewBox="0 0 11 13"><rect x="1" y="1" width="9" height="11" fill="none" stroke="#fff" stroke-width="1.2"/><line x1="3" y1="5" x2="8" y2="5" stroke="#fff"/><line x1="3" y1="8" x2="8" y2="8" stroke="#fff"/></svg></span>Recent News</div>
    <span class="readmore">Read More</span>
    <p class="para" style="top:45px">Lorem Ipsum is simply dummy text of the printing &amp; type-setting industry. Lorem Ipsum has been the industry's</p>
    <div class="dash" style="top:82px"></div>
    <p class="para" style="top:93px">Lorem Ipsum is simply dummy text of the printing &amp; type-setting industry. Lorem Ipsum has been the industry's</p>
    <div class="dash" style="top:130px"></div>
    <p class="para" style="top:142px">Lorem Ipsum is simply dummy text of the printing &amp; type-setting industry. Lorem Ipsum has been the industry's</p>
  </div>

  <!-- help -->
  <div class="abs help">
    <div class="help-head"><svg style="position:absolute;left:8px;top:7px" width="16" height="14" viewBox="0 0 16 14"><circle cx="6" cy="4" r="3" fill="#fff"/><path d="M0 13 C0 8 12 8 12 13Z" fill="#fff"/><circle cx="11.5" cy="3.5" r="2.3" fill="#fff"/></svg>NEED ANY HELP</div>
    <div class="cond" style="margin-top:14px;font-size:11px;font-weight:700">Call Toll Free</div>
    <div class="cond" style="font-size:23px;margin-top:2px">1234567890</div>
    <div class="cond" style="font-size:10.5px;margin-top:4px">Our expert always ready to help you</div>
  </div>
  <div class="abs tuned">
    <div style="margin-top:10px">STAY TUNED WITH US</div>
    <div style="display:flex;justify-content:center;gap:7px;margin-top:9px"><span class="social"></span><span class="social"></span><span class="social"></span></div>
  </div>

  <!-- banners -->
  <div class="abs photo" role="img" aria-label="Driver's view of dashboard and sunny road" style="left:231px;top:916px;width:171px;height:112px;background:linear-gradient(180deg,#c9d6e0,#7c8a4a 55%,#2a2a2a)"></div>
  <div class="abs photo" role="img" aria-label="White car front view" style="left:410px;top:916px;width:171px;height:112px;background:linear-gradient(180deg,#ffffff,#d9dbdd)"></div>
  <div class="abs photo" role="img" aria-label="Red sports car on dark background" style="left:586px;top:916px;width:172px;height:112px;background:linear-gradient(135deg,#d4202c,#1a0a0c)"></div>
  <div class="abs photo" role="img" aria-label="Silver car in motion" style="left:762px;top:916px;width:171px;height:112px;background:linear-gradient(135deg,#c7cbcf,#5f666c)"></div>

  <!-- newsletter -->
  <div class="abs newsletter-band"></div>
  <div class="abs nl-title">SUBSCRIBE TO OUR NEWSLETTER FEED</div>
  <div class="abs nl-sub">Want to hear about new more ? just enter your email address.</div>
  <div class="abs nl-form">
    <div class="abs nl-input">please enter your email address</div>
    <svg class="abs" style="left:15px;top:14px" width="20" height="14" viewBox="0 0 20 14"><rect x="0.5" y="0.5" width="19" height="13" fill="#fff" stroke="#aaa"/><path d="M1 1 L10 8 L19 1" fill="none" stroke="#aaa"/></svg>
    <div class="abs btn nl-btn">SUBSCRIBE</div>
  </div>

  <!-- footer -->
  <div class="abs footer"><span>Home</span><span>About us</span><span>New cars</span><span>Used cars</span><span>Custoers Reviews</span><span>Recent News</span><span>Contact Us</span></div>
  <div class="abs copy">Copyrights @ 2014 All rights reserved.</div>
</div>
</body>
</html>
```